BWH Business Card Design

We are a small construction equipment rental and hardware store located in Middle Tennessee. We have three stores. Our primary business is construction equipment. We have an existing logo we'd like to use. I think I would like to list each store physical address on the back of the card and maybe the web address also: www.bwhrentco.example.

We also need a design that we can incorporate into company letterhead, small note pads, and even checks if possible.

Industry/Entity Type

Construction

Contact Information for Business Card

We have our Logo, Name: Bramwell Hoisting Works, Employee Name, Main Phone Number, Mobile Phone Number, Email Address, Company Address, and website information (There are three locations that can go on the back if necessary) We would like to leave some room on the back of the card in case we want to write information down on it.

```html
<!DOCTYPE html>
<html lang="en">
<head>
<meta charset="utf-8">
<title>BWH Business Card</title>
<link rel="stylesheet" href="https://fonts.googleapis.com/css2?family=Montserrat:wght@700;800&family=Open+Sans:wght@400;600&display=swap">
<style>
  :root {
    --backdrop: #e6e3df;
    --card: #ffffff;
    --card-edge: #d9d9d9;
    --brand-red: #e8283a;
    --brand-navy: #1f2d5e;
    --slate: #5a5f6b;
    --ink: #141414;
  }
  * { box-sizing: border-box; margin: 0; padding: 0; }
  html, body {
    width: 1200px; height: 997px; overflow: hidden;
    background: var(--backdrop);
  }
  .stage { position: relative; width: 1200px; height: 997px; }
  .card {
    position: absolute; width: 560px; height: 320px;
    background: var(--card);
    box-shadow: 0 10px 28px rgba(0,0,0,.16);
    border: 1px solid var(--card-edge);
    overflow: hidden;
  }
  .card--front { left: 110px; top: 140px; }
  .card--back  { left: 530px; top: 520px; }

  .brand { display: flex; align-items: center; gap: 10px; }
  .brand__dot {
    width: 44px; height: 44px; border-radius: 50%;
    background: var(--brand-red);
  }
  .brand__name {
    font-family: "Montserrat", sans-serif; font-weight: 800;
    font-size: 30px; color: var(--brand-navy); letter-spacing: 1px;
  }
  .company {
    font-family: "Montserrat", sans-serif; font-weight: 700;
    color: var(--slate); text-transform: uppercase; line-height: 1.1;
  }

  .card--front .front__content {
    position: absolute; inset: 0;
    display: flex; flex-direction: column; align-items: center; justify-content: center;
    gap: 14px;
  }
  .card--front .company { font-size: 21px; text-align: center; }
  .front__web {
    font-family: "Open Sans", sans-serif; font-weight: 600;
    font-size: 14px; color: var(--brand-red);
  }

  .back__swoosh { position: absolute; inset: 0; }
  .back__brand { position: absolute; left: 60px; top: 80px; display: flex; flex-direction: column; align-items: center; gap: 10px; }
  .card--back .company { font-size: 16px; text-align: center; }
  .employee {
    position: absolute; right: 36px; top: 32px;
    font-family: "Open Sans", sans-serif; font-size: 17px; color: var(--ink);
  }
  .contact {
    position: absolute; right: 20px; top: 118px;
    list-style: none; text-align: right;
    font-family: "Open Sans", sans-serif; font-size: 14px; line-height: 21px; color: var(--ink);
  }
  .contact li { display: flex; justify-content: flex-end; align-items: center; gap: 6px; }
  .contact svg { width: 11px; height: 11px; }
  .address {
    position: absolute; right: 20px; bottom: 40px;
    font-family: "Open Sans", sans-serif; font-weight: 600; font-size: 13px; color: var(--ink);
  }
</style>
</head>
<body>
<main class="stage">

  <section class="card card--front">
    <div class="front__content">
      <div class="brand">
        <span class="brand__dot"></span>
        <span class="brand__name">BWH</span>
      </div>
      <p class="company">Bramwell Hoisting<br>Works</p>
      <p class="front__web">www.bwhrentco.example</p>
    </div>
  </section>

  <section class="card card--back">
    <svg class="back__swoosh" viewBox="0 0 560 320" width="560" height="320" aria-hidden="true">
      <path d="M110 320 C250 300 300 150 390 80 C450 40 510 30 560 22 L560 320 Z" fill="var(--brand-red)"/>
      <path d="M150 300 C270 270 310 150 400 95 C450 65 500 50 545 40 C490 60 440 80 400 115 C320 190 290 280 150 300 Z" fill="#fff"/>
      <path d="M0 268 C110 262 180 220 220 150 C200 230 120 285 0 292 Z" fill="var(--brand-navy)"/>
    </svg>

    <div class="back__brand">
      <div class="brand">
        <span class="brand__dot"></span>
        <span class="brand__name">BWH</span>
      </div>
      <p class="company">Bramwell Hoisting<br>Works</p>
    </div>

    <p class="employee">EMPLOYEE NAME</p>

    <ul class="contact">
      <li>XXX XXX XXXX <svg viewBox="0 0 12 12"><rect x="2" y="1" width="8" height="10" rx="1" fill="none" stroke="#fff" stroke-width="1.5"/></svg></li>
      <li>XXX XXX XXXX <svg viewBox="0 0 12 12"><path d="M2 4 Q6 0 10 4 L9 6 L7 5 L5 5 L3 6 Z M3 7 H9 V11 H3 Z" fill="#fff"/></svg></li>
      <li>info@mailbox.example <svg viewBox="0 0 12 12"><rect x="1" y="3" width="10" height="7" fill="#fff"/><path d="M1 3 L6 7 L11 3" fill="none" stroke="var(--brand-red)" stroke-width="1"/></svg></li>
      <li>www.bwhrentco.example <svg viewBox="0 0 12 12"><circle cx="6" cy="6" r="5" fill="#fff"/><path d="M1 6 H11 M6 1 V11" stroke="var(--brand-red)" stroke-width="1"/></svg></li>
      <li>&nbsp;<svg viewBox="0 0 12 12"><path d="M1 6 L6 1 L11 6 H9.5 V11 H2.5 V6 Z" fill="#fff"/></svg></li>
    </ul>

    <p class="address">Your Address Inc 2nd Lane Ave Millbrook, TN 00000</p>
  </section>

</main>
</body>
</html>
```